We would like to have a poster designed for our new fitness program called " Steady Core Course ". It consists of 1 assessment by a registered physiotherapist and 5 closely monitored exercise sessions. the goal of the program is to develop a strong back to meed the daily demands and sport activities. Ideal program for the people who sit all day for work. Green is our theme color of the clinic. We are open for other colors as well.The poster design should communicate fitness and strength. One time cost of the program is $ 350 . We will see the patient once per week for 6 weeks.

Target Market(s)

People with sitting job and heavy labor job.
Athelets
Active individuals who wanna participate in yoga, running, fitness classes etc.

Industry/Entity Type

Fitness

Font styles to use
Serif

Requirements
Must have
• simplicity and strong message.
Nice to have
• pain free spine picture

```html
<!DOCTYPE html>
<html lang="en">
<head>
<meta charset="utf-8">
<title>Steady Core Course Poster</title>
<link href="https://fonts.googleapis.com/css2?family=Oswald:wght@500;600&family=Roboto+Condensed:ital,wght@1,700;1,800&display=swap" rel="stylesheet">
<style>
  :root {
    --bg-deep: #012e12;
    --bg-mid: #06622a;
    --bg-glow: #1f9a3e;
    --spine-glow: #b6f06a;
    --white: #ffffff;
    --cream: #f6f2a6;
    --yellow: #f3ef6a;
    --lime: #c9e27c;
    --box-fill: rgba(132, 160, 40, 0.72);
    --box-edge: rgba(230, 240, 170, 0.85);
  }
  html, body {
    margin: 0;
    padding: 0;
    width: 848px;
    height: 1200px;
    overflow: hidden;
    background: var(--bg-deep);
  }
  .poster {
    position: relative;
    width: 848px;
    height: 1200px;
    overflow: hidden;
    background:
      radial-gradient(ellipse 55% 60% at 50% 45%, var(--bg-mid) 0%, rgba(6, 98, 42, 0) 100%),
      linear-gradient(180deg, #024a1d 0%, var(--bg-deep) 100%);
    text-align: center;
    font-family: "Roboto Condensed", "Arial Narrow", sans-serif;
  }
  .spine-art {
    position: absolute;
    left: 214px;
    top: 0;
    width: 420px;
    height: 1200px;
    background:
      radial-gradient(ellipse 14% 42% at 50% 50%, rgba(182, 240, 106, 0.55) 0%, rgba(182, 240, 106, 0) 100%),
      radial-gradient(ellipse 50% 55% at 50% 70%, rgba(31, 154, 62, 0.55) 0%, rgba(31, 154, 62, 0) 100%);
  }
  .title {
    position: absolute;
    left: 0;
    width: 100%;
    margin: 0;
    font-family: "Oswald", "Arial Narrow", sans-serif;
    font-weight: 600;
    text-transform: uppercase;
    line-height: 1;
  }
  .title-top { top: 36px; font-size: 84px; color: var(--white); letter-spacing: 1px; }
  .title-main { top: 120px; font-size: 132px; color: var(--cream); letter-spacing: 2px; }

  .line {
    position: absolute;
    left: 0;
    width: 100%;
    margin: 0;
    font-style: italic;
    font-weight: 800;
    line-height: 1;
  }
  .assessment { top: 266px; font-size: 50px; color: var(--yellow); }
  .physio { top: 344px; font-size: 30px; color: var(--white); font-weight: 700; }
  .sessions { top: 384px; font-size: 44px; color: var(--yellow); }
  .sessions-sub { top: 430px; font-size: 38px; color: var(--yellow); }

  .audience-box {
    position: absolute;
    left: 82px;
    top: 560px;
    width: 690px;
    height: 236px;
    box-sizing: border-box;
    border: 3px solid var(--box-edge);
    border-radius: 36px;
    background: var(--box-fill);
    display: flex;
    align-items: center;
    justify-content: center;
  }
  .audience-box p {
    margin: 0;
    font-style: italic;
    font-weight: 800;
    font-size: 48px;
    line-height: 1.3;
    color: var(--white);
  }
  .cost-label { top: 870px; font-size: 31px; color: var(--white); font-weight: 700; }
  .price { top: 930px; font-size: 70px; color: var(--white); }
  .schedule { top: 1040px; font-size: 44px; color: var(--lime); line-height: 1.58; }
</style>
</head>
<body>
  <main class="poster">
    <div class="spine-art" role="img" aria-label="Glowing green illustration of a healthy, pain-free spine"></div>

    <h1 class="title title-top">Steady Core</h1>
    <p class="title title-main">Course</p>

    <p class="line assessment">1 assessment</p>
    <p class="line physio">by a registered physiotherapist and</p>
    <p class="line sessions">5 closely monitored</p>
    <p class="line sessions-sub">exercise sessions</p>

    <div class="audience-box">
      <p>Ideal program for the people<br>who sit all day for work.</p>
    </div>

    <p class="line cost-label">One time cost of the program is</p>
    <p class="line price">$ 350</p>
    <p class="line schedule">We will see the patient<br>once per week for 6 weeks.</p>
  </main>
</body>
</html>
```